Christmas Collection Candle Label Design

Looking to update our existing Christmas Candle Collection labels. Labels should reflect the overall feel of our brand- www.wickmerelane.ca
Want to include some color elements. Holiday colors added into design but more muted/ earthy tones not vibrant colors . Metallic elements and line art botanical illustration. Fonts should be more align to brand
Scents
Holiday Tree
Candy Cane
Sugar and Spice
Joyeaux Noel

```html
<!DOCTYPE html>
<html lang="en">
<head>
<meta charset="utf-8">
<title>Wickmere Lane — Christmas Collection Labels</title>
<link rel="stylesheet" href="https://fonts.googleapis.com/css2?family=Gelasio:wght@400;500&display=swap">
<style>
  :root {
    --bg-top: #d8d8d8;
    --bg-bottom: #e6ddd4;
    --paper: #ffffff;
    --gold-1: #e9c97a;
    --gold-2: #fbeaa2;
    --gold-3: #f2cf73;
    --ink: #3a2a20;
    --sketch: rgba(170, 170, 170, 0.17);
    --peach: rgba(250, 190, 130, 0.30);

    --tree-frame: #558a4f;
    --tree-title: #6f9c6a;
    --tree-sub: #9fcb94;

    --cane-frame: #c25e60;
    --cane-title: #7e3e42;
    --cane-sub: #d4a0a0;

    --spice-frame: #bf7658;
    --spice-title: #7a5242;
    --spice-sub: #cdb39b;

    --noel-frame: #5a8fc1;
    --noel-title: #3e4d7e;
    --noel-sub: #9aa3d2;
  }
  * { box-sizing: border-box; margin: 0; padding: 0; }
  html, body { width: 1173px; height: 1200px; overflow: hidden; }
  body {
    background: linear-gradient(180deg, var(--bg-top), var(--bg-bottom));
    font-family: "Gelasio", Georgia, serif;
    position: relative;
  }
  .label {
    position: absolute;
    width: 487px;
    height: 487px;
    background: var(--paper);
    border: 10px solid var(--frame);
    box-shadow: 0 18px 22px rgba(0,0,0,0.18);
    overflow: hidden;
  }
  .label--tree  { left: 77px;  top: 74px;  --frame: var(--tree-frame);  --title: var(--tree-title);  --sub: var(--tree-sub); }
  .label--cane  { left: 606px; top: 74px;  --frame: var(--cane-frame);  --title: var(--cane-title);  --sub: var(--cane-sub); }
  .label--spice { left: 77px;  top: 611px; --frame: var(--spice-frame); --title: var(--spice-title); --sub: var(--spice-sub); }
  .label--noel  { left: 606px; top: 611px; --frame: var(--noel-frame);  --title: var(--noel-title);  --sub: var(--noel-sub); }

  .gold-frame {
    position: absolute;
    left: 15px; top: 15px; right: 15px; bottom: 15px;
    border: 4px solid transparent;
    border-image: linear-gradient(135deg, var(--gold-1), var(--gold-2), var(--gold-3), var(--gold-2)) 1;
    z-index: 1;
  }
  .sketch-art {
    position: absolute;
    background: var(--sketch);
    border-radius: 38% 46% 40% 50%;
  }
  .hero-art {
    position: absolute;
    background: var(--peach);
    border-radius: 42% 36% 46% 40%;
  }
  .brand, .title, .est, .year, .facts { z-index: 2; }
  .brand {
    position: absolute;
    left: 0; right: 0; top: 53px;
    text-align: center;
    font-size: 13px;
    letter-spacing: 0.4px;
    color: var(--ink);
  }
  .title {
    position: absolute;
    left: 0; right: 0; top: 132px;
    text-align: center;
    color: var(--title);
    font-size: 72px;
    line-height: 67px;
    font-weight: 500;
    letter-spacing: 1px;
    text-transform: uppercase;
  }
  .title .small { text-transform: none; font-size: 54px; letter-spacing: 0; }
  .est, .year {
    position: absolute;
    top: 290px;
    font-size: 29px;
    color: var(--sub);
    letter-spacing: 1px;
  }
  .est  { left: 75px; }
  .year { right: 56px; }
  .facts {
    position: absolute;
    left: 32px; right: 32px; top: 397px;
    display: flex; gap: 5px;
    height: 47px;
  }
  .fact {
    flex: 1;
    display: flex; align-items: center; justify-content: center;
    text-align: center;
    font-size: 13px;
    line-height: 12.5px;
    color: var(--ink);
    background: linear-gradient(120deg, var(--gold-3), var(--gold-2) 55%, var(--gold-3));
  }
  .fact:first-child { flex: 0 0 132px; }
  .fact:nth-child(2) { flex: 0 0 144px; }
  .fact:last-child { background: linear-gradient(120deg, var(--gold-3), var(--gold-2) 70%, #fff8e4); }
</style>
</head>
<body>

  <section class="label label--tree">
    <div class="sketch-art" role="img" aria-label="Line-art holly leaves and berries" style="left:0;top:-8px;width:205px;height:128px;"></div>
    <div class="sketch-art" role="img" aria-label="Line-art pine cone" style="left:-10px;top:212px;width:92px;height:210px;"></div>
    <div class="sketch-art" role="img" aria-label="Line-art flowering botanical sprig" style="left:322px;top:8px;width:150px;height:225px;"></div>
    <div class="hero-art" role="img" aria-label="Peach line-art leafy botanical branch" style="left:125px;top:262px;width:228px;height:210px;"></div>
    <div class="gold-frame"></div>
    <p class="brand">WICKMERE LANE</p>
    <h2 class="title">Holiday<br>Tree</h2>
    <span class="est">EST</span><span class="year">2005</span>
    <div class="facts">
      <div class="fact">Marketplace<br>connection</div>
      <div class="fact">Made with pure<br>essential oil</div>
      <div class="fact">Net weight: 120g</div>
    </div>
  </section>

  <section class="label label--cane">
    <div class="sketch-art" role="img" aria-label="Line-art candy cane with holly" style="left:12px;top:36px;width:100px;height:154px;"></div>
    <div class="sketch-art" role="img" aria-label="Line-art small ribbon bow" style="left:192px;top:86px;width:74px;height:46px;"></div>
    <div class="sketch-art" role="img" aria-label="Line-art candy cane with holly and ribbon" style="left:318px;top:-10px;width:160px;height:234px;"></div>
    <div class="sketch-art" role="img" aria-label="Line-art ribbon bow" style="left:0;top:240px;width:96px;height:150px;"></div>
    <div class="sketch-art" role="img" aria-label="Line-art candy cane" style="left:398px;top:236px;width:80px;height:148px;"></div>
    <div class="hero-art" role="img" aria-label="Peach line-art candy cane with bow" style="left:158px;top:264px;width:164px;height:176px;"></div>
    <div class="gold-frame"></div>
    <p class="brand">WICKMERE LANE</p>
    <h2 class="title">Candy<br>Cane</h2>
    <span class="est">EST</span><span class="year">2005</span>
    <div class="facts">
      <div class="fact">Marketplace<br>connection</div>
      <div class="fact">Made with pure<br>essential oil</div>
      <div class="fact">Net weight: 120g</div>
    </div>
  </section>

  <section class="label label--spice">
    <div class="sketch-art" role="img" aria-label="Line-art bay leaves" style="left:3px;top:41px;width:152px;height:92px;"></div>
    <div class="sketch-art" role="img" aria-label="Line-art wrapped sweet" style="left:290px;top:81px;width:64px;height:46px;"></div>
    <div class="sketch-art" role="img" aria-label="Line-art chili pepper" style="left:372px;top:1px;width:88px;height:152px;"></div>
    <div class="sketch-art" role="img" aria-label="Line-art star anise" style="left:34px;top:195px;width:84px;height:90px;"></div>
    <div class="sketch-art" role="img" aria-label="Line-art rosemary sprigs" style="left:332px;top:140px;width:140px;height:250px;"></div>
    <div class="sketch-art" role="img" aria-label="Line-art herb sprig" style="left:24px;top:290px;width:56px;height:100px;"></div>
    <div class="hero-art" role="img" aria-label="Peach line-art chili pepper and wrapped candy" style="left:117px;top:263px;width:198px;height:118px;"></div>
    <div class="gold-frame"></div>
    <p class="brand">WICKMERE LANE</p>
    <h2 class="title">Sugar <span class="small">and</span><br>Spice</h2>
    <span class="est">EST</span><span class="year">2005</span>
    <div class="facts">
      <div class="fact">Marketplace<br>connection</div>
      <div class="fact">Made with pure<br>essential oil</div>
      <div class="fact">Net weight: 120g</div>
    </div>
  </section>

  <section class="label label--noel">
    <div class="sketch-art" role="img" aria-label="Line-art holly leaves and berries" style="left:-9px;top:-5px;width:166px;height:138px;"></div>
    <div class="sketch-art" role="img" aria-label="Line-art snowflake" style="left:312px;top:10px;width:84px;height:78px;"></div>
    <div class="sketch-art" role="img" aria-label="Line-art Santa hat" style="left:370px;top:57px;width:74px;height:56px;"></div>
    <div class="sketch-art" role="img" aria-label="Line-art snowflake" style="left:-9px;top:247px;width:96px;height:118px;"></div>
    <div class="sketch-art" role="img" aria-label="Line-art poinsettia flower" style="left:379px;top:297px;width:98px;height:100px;"></div>
    <div class="hero-art" role="img" aria-label="Peach line-art Christmas bells with bow" style="left:142px;top:257px;width:186px;height:122px;"></div>
    <div class="gold-frame"></div>
    <p class="brand">WICKMERE LANE</p>
    <h2 class="title">Joyeaux<br>Noel</h2>
    <span class="est">EST</span><span class="year">2005</span>
    <div class="facts">
      <div class="fact">Marketplace<br>connection</div>
      <div class="fact">Made with pure<br>essential oil</div>
      <div class="fact">Net weight: 120g</div>
    </div>
  </section>

</body>
</html>
```